依頼概要
チラシ/ポスターデータ制作の依頼です。
カブトムシ・クワガタムシの選挙用ポスター・消しゴム用スリーブを作成していただきたいです。
一度ラフデザインは出していて、それに対して修正指示がきています。
そのため修正指示をもとに、全体的にクオリティを上げていただければと思っています。
また、消しゴム用スリーブに関しては、ポスターのイメージが固まり次第、
背景などを流用していただく形になります。

※補足
全部で30種類のポスターがあります。
一度、2種類のポスターを作成していただき、こちらのイメージと一番近い方に、残り28種類のポスター・消しゴム用スリーブを作成していただきます。

●イベント概要
・子ども向け昆虫イベントです。
・30種類のカブトムシ・クワガタムシを飼育展示しながら選挙形式で、自分のお気に入りのカブトムシ・クワガタムシに投票します。
・そのイベントに付随した、制作物の作成をお願いいたします。

●仕様・ページ数
・ポスターA3 1ページ(片面)*30種類
・消しゴム用スリーブ(デザイン流用)小 42.5mm*17.5mm *30種
・消しゴム用スリーブ(デザイン流用)大 52.5mm*23.75mm *30種
※消しゴムは、大小サイズ調整をしていただくだけで構いません。

●備考
・パッと見たときに色が被らずに見えるようにお願いします。
・子どもが見たときにワクワクするようなデザインが望ましいです。

●支給できるもの
・ポスターラフデザイン(Ai)
http://pelvanadrop.jp/download/c83915a2dd6e4b1fa07c3e9b5d21a8ce47f90b3d

・消しゴムラフデザイン(Ai)
http://pelvanadrop.jp/download/61b48e2f9a3c07d5e18b24f6c9d0a3e7b5f12c84

・昆虫写真(EPS/PSD)
https://17.tomuvault.nu/0708-kq82de917c3b5f0a6e2d48b1c7e9a260f

・修正指示(PDF)
http://pelvanadrop.jp/download/9e2c60a4b7d1f38e05a9c2b6d4f7e18a3c50b9d2

・参考制作事例(完成イメージのポスター5種類)

```html
<!DOCTYPE html>
<html lang="ja">
<head>
<meta charset="UTF-8">
<title>グラントシロカブト｜昆虫ヒーロー大投票</title>
<link href="https://fonts.googleapis.com/css2?family=Dela+Gothic+One&family=M+PLUS+Rounded+1c:wght@800;900&display=swap" rel="stylesheet">
<style>
  :root {
    --ink: #111111;
    --white: #ffffff;
    --paper: #f2f2f2;
    --mist: #b9b9b9;
    --shadow-brown: #2a1d14;
    --deep: #0d0907;
    --gold: #f4c51c;
    --gold-deep: #b87a04;
    --beetle-dark: #1b1812;
    --beetle-olive: #6d6a4e;
    --beetle-sheen: #d9d6c8;
  }
  html, body {
    margin: 0;
    padding: 0;
    width: 849px;
    height: 1200px;
    overflow: hidden;
    background: var(--deep);
  }
  .poster {
    position: relative;
    width: 849px;
    height: 1200px;
    overflow: hidden;
    background:
      linear-gradient(180deg, rgba(0,0,0,0) 0%, rgba(0,0,0,0) 55%, rgba(42,29,20,0.85) 80%, var(--deep) 100%),
      radial-gradient(ellipse at 62% 58%, var(--white) 0%, var(--paper) 30%, var(--mist) 75%, #8a8a8a 100%);
    font-family: "Dela Gothic One", sans-serif;
  }
  .rays {
    position: absolute;
    inset: 0;
    background: repeating-conic-gradient(from 0deg at 62% 58%, rgba(255,255,255,0.55) 0deg 4deg, rgba(255,255,255,0) 4deg 11deg);
    mask-image: radial-gradient(circle at 62% 58%, #000 0%, #000 40%, transparent 75%);
    -webkit-mask-image: radial-gradient(circle at 62% 58%, #000 0%, #000 40%, transparent 75%);
  }
  .flare {
    position: absolute;
    width: 150px;
    height: 150px;
    border-radius: 50%;
    background: radial-gradient(circle, #fff 0%, rgba(255,255,255,0.7) 15%, rgba(255,255,255,0) 60%);
  }
  .flare--left { left: -10px; top: -10px; }
  .flare--right { right: -20px; top: -5px; }

  .event-name {
    position: absolute;
    top: 62px;
    left: 0;
    width: 100%;
    display: flex;
    justify-content: center;
    align-items: center;
    gap: 14px;
    font-size: 40px;
    color: var(--shadow-brown);
  }
  .event-name__mark {
    width: 22px;
    height: 22px;
    border-radius: 50%;
    background: var(--gold);
  }

  .beetle-photo {
    position: absolute;
    left: -20px;
    top: 330px;
    width: 860px;
    height: 610px;
    border-radius: 45% 55% 40% 50% / 55% 45% 55% 45%;
    background:
      radial-gradient(ellipse at 42% 40%, var(--beetle-sheen) 0%, var(--beetle-olive) 25%, var(--beetle-dark) 55%, rgba(27,24,18,0) 72%);
  }

  .tagline {
    margin: 0;
    font-weight: 400;
  }
  .tagline__part {
    position: absolute;
    white-space: nowrap;
    line-height: 1;
    paint-order: stroke fill;
  }
  .tagline__white {
    left: 40px;
    top: 290px;
    font-size: 84px;
    color: var(--white);
    -webkit-text-stroke: 14px var(--ink);
    transform: rotate(-12deg);
    transform-origin: left center;
  }
  .tagline__shine {
    left: 205px;
    top: 215px;
    font-size: 120px;
    color: var(--white);
    -webkit-text-stroke: 16px var(--ink);
    transform: rotate(-12deg);
    transform-origin: left center;
  }
  .tagline__legend {
    left: 18px;
    top: 420px;
    font-size: 112px;
    color: var(--gold);
    -webkit-text-stroke: 14px var(--ink);
    text-shadow: 5px 6px 0 var(--gold-deep);
    transform: rotate(-6deg);
    transform-origin: left center;
  }
  .tagline__rest {
    left: 240px;
    top: 340px;
    font-family: "M PLUS Rounded 1c", sans-serif;
    font-weight: 900;
    font-size: 72px;
    color: var(--ink);
    -webkit-text-stroke: 10px var(--white);
    transform: rotate(-16deg);
    transform-origin: left center;
  }

  .species-name {
    position: absolute;
    left: 0;
    bottom: 18px;
    width: 100%;
    margin: 0;
    font-weight: 400;
    text-align: center;
    line-height: 1.05;
  }
  .species-name__line {
    display: block;
    font-size: 150px;
    letter-spacing: 0.02em;
    white-space: nowrap;
    color: var(--white);
    -webkit-text-stroke: 18px var(--ink);
    paint-order: stroke fill;
    text-shadow: 0 0 6px rgba(255,255,255,0.9);
  }
  .species-name__line--second { font-size: 160px; }
  .species-name__accent { color: var(--gold); }
</style>
</head>
<body>
  <main class="poster">
    <div class="rays"></div>
    <div class="flare flare--left"></div>
    <div class="flare flare--right"></div>

    <div class="event-name">
      <span class="event-name__mark"></span>
      <span>昆虫ヒーロー大投票</span>
    </div>

    <div class="beetle-photo" role="img" aria-label="長い角を持つ白いグラントシロカブトの写真"></div>

    <h2 class="tagline">
      <span class="tagline__part tagline__white">白く</span>
      <span class="tagline__part tagline__shine">輝く</span>
      <span class="tagline__part tagline__rest">のカブトムシ</span>
      <span class="tagline__part tagline__legend">伝説</span>
    </h2>

    <h1 class="species-name">
      <span class="species-name__line">グラント</span>
      <span class="species-name__line species-name__line--second">シロ<span class="species-name__accent">カ</span>ブト</span>
    </h1>
  </main>
</body>
</html>
```